HML5 Web Application Design

We need a graphic design to give a HTML web application a modern look and feel. The design should be clean and neat with a metro inspired interface. All application uses vormanta controls so any experience with these would be great.
Perhaps you could also include a few screenshots of your previous work

Industry/Entity Type

Graphic Design

Requirements
Must have
• Must be HTML 5 compliant

```html
<!DOCTYPE html>
<html lang="en">
<head>
<meta charset="utf-8">
<title>clipforge – Login</title>
<link href="https://fonts.googleapis.com/css2?family=Open+Sans:wght@300;400;600&display=swap" rel="stylesheet">
<style>
  :root {
    --header-bg: #ffffff;
    --page-bg: #f4f4f4;
    --footer-bg: #e0e0e0;
    --divider: #cfcfcf;
    --nav-bg: #f0f0f0;
    --nav-text: #666666;
    --title: #3b63c9;
    --muted: #8a8a8a;
    --text: #333333;
    --placeholder: #a8a8a8;
    --icon: #c4c4c4;
    --field-border: #dddddd;
    --focus-border: #86c6e4;
    --accent: #56aed6;
    --accent-border: #3f93ba;
    --secondary-bg: #f0f0f0;
    --secondary-border: #cccccc;
    --brand: #222222;
    --brand-mark: #ef4a3a;
  }
  * { box-sizing: border-box; margin: 0; padding: 0; }
  html, body { width: 1200px; height: 513px; overflow: hidden; }
  body { position: relative; font-family: "Open Sans", sans-serif; font-weight: 300; color: var(--text); background: var(--page-bg); }

  .site-header { position: absolute; left: 0; top: 0; width: 1200px; height: 94px; background: var(--header-bg); }
  .brand { position: absolute; left: 70px; top: 34px; display: flex; align-items: center; gap: 10px; font-size: 29px; font-weight: 400; color: var(--brand); letter-spacing: -0.5px; }
  .brand-mark { width: 22px; height: 22px; border-radius: 50%; background: var(--brand-mark); }
  .main-nav { position: absolute; left: 334px; top: 33px; display: flex; gap: 9px; }
  .main-nav a { display: block; height: 36px; line-height: 36px; padding: 0 9px; background: var(--nav-bg); color: var(--nav-text); font-size: 14px; text-decoration: none; border-radius: 2px; }

  .divider { position: absolute; left: 617px; top: 94px; width: 3px; height: 383px; background: var(--divider); }

  .login-panel { position: absolute; top: 94px; width: 600px; height: 383px; }
  .login-panel.left { left: 0; }
  .login-panel.right { left: 600px; }
  .login-title { position: absolute; left: 67px; top: 12px; font-size: 41px; font-weight: 300; color: var(--title); }
  .login-subtitle { position: absolute; left: 67px; top: 68px; font-size: 14px; color: var(--muted); }

  .field { position: absolute; left: 67px; width: 365px; height: 46px; background: #fff; border: 1px solid var(--field-border); display: flex; align-items: center; }
  .field.username { top: 121px; }
  .field.password { top: 181px; }
  .field.focused { border-color: var(--focus-border); box-shadow: 0 0 4px rgba(86,174,214,0.55); }
  .field svg { margin-left: 10px; margin-right: 6px; flex: none; }
  .field-value { font-size: 21px; color: var(--text); font-weight: 400; }
  .field-placeholder { font-size: 20px; color: var(--placeholder); }
  .field-help { position: absolute; right: 0; top: 6px; height: 34px; width: 23px; border-left: 1px solid var(--field-border); text-align: center; line-height: 34px; font-size: 14px; font-weight: 600; color: var(--muted); }

  .remember { position: absolute; left: 70px; top: 261px; display: flex; align-items: center; gap: 9px; font-size: 16px; color: var(--text); }
  .checkbox { width: 21px; height: 21px; border: 1px solid #555; background: #fff; }

  .btn { position: absolute; left: 294px; width: 116px; height: 39px; line-height: 37px; text-align: center; font-size: 16px; }
  .btn-primary { top: 248px; background: var(--accent); border: 1px solid var(--accent-border); color: #fff; }
  .btn-secondary { top: 318px; background: var(--secondary-bg); border: 1px solid var(--secondary-border); color: var(--muted); }

  .separator { position: absolute; left: 67px; top: 317px; width: 375px; height: 1px; background: linear-gradient(to right, rgba(220,220,220,0), #dcdcdc 25%, #dcdcdc 75%, rgba(220,220,220,0)); }
  .signup-prompt { position: absolute; right: 329px; top: 328px; font-size: 16px; color: var(--text); }

  .site-footer { position: absolute; left: 0; top: 477px; width: 1200px; height: 36px; background: var(--footer-bg); }
  .site-footer p { position: absolute; left: 68px; top: 8px; font-size: 13px; color: var(--muted); }
</style>
</head>
<body>
  <header class="site-header">
    <div class="brand"><span class="brand-mark"></span>clipforge</div>
    <nav class="main-nav">
      <a href="#">Register</a>
      <a href="#">Log in</a>
      <a href="#">Request Pin</a>
    </nav>
  </header>

  <section class="login-panel left">
    <h1 class="login-title">Login</h1>
    <p class="login-subtitle">Use a local account to login</p>
    <div class="field username">
      <svg width="16" height="18" viewBox="0 0 16 18"><circle cx="8" cy="5" r="4" fill="var(--icon)"/><path d="M0 18c0-5 3.5-7.5 8-7.5s8 2.5 8 7.5z" fill="var(--icon)"/></svg>
      <span class="field-placeholder">username</span>
    </div>
    <div class="field password">
      <svg width="14" height="17" viewBox="0 0 14 17"><path d="M3 7V5a4 4 0 0 1 8 0v2" fill="none" stroke="var(--icon)" stroke-width="2"/><rect x="1" y="7" width="12" height="10" rx="1" fill="var(--icon)"/></svg>
      <span class="field-placeholder">password</span>
      <span class="field-help">?</span>
    </div>
    <label class="remember"><span class="checkbox"></span>Remember me?</label>
    <div class="btn btn-primary">Login</div>
    <div class="separator"></div>
    <p class="signup-prompt">Don't have an account?</p>
    <div class="btn btn-secondary">Sign Up</div>
  </section>

  <div class="divider"></div>

  <section class="login-panel right">
    <h1 class="login-title">Login</h1>
    <p class="login-subtitle">Use a local account to login</p>
    <div class="field username focused">
      <svg width="16" height="18" viewBox="0 0 16 18"><circle cx="8" cy="5" r="4" fill="var(--icon)"/><path d="M0 18c0-5 3.5-7.5 8-7.5s8 2.5 8 7.5z" fill="var(--icon)"/></svg>
      <span class="field-value">Alan Mercer</span>
    </div>
    <div class="field password">
      <svg width="14" height="17" viewBox="0 0 14 17"><path d="M3 7V5a4 4 0 0 1 8 0v2" fill="none" stroke="var(--icon)" stroke-width="2"/><rect x="1" y="7" width="12" height="10" rx="1" fill="var(--icon)"/></svg>
      <span class="field-placeholder">password</span>
      <span class="field-help">?</span>
    </div>
    <label class="remember"><span class="checkbox"></span>Remember me?</label>
    <div class="btn btn-primary">Login</div>
    <div class="separator"></div>
    <p class="signup-prompt">Don't have an account?</p>
    <div class="btn btn-secondary">Sign Up</div>
  </section>

  <footer class="site-footer"><p>©2013 - ORV</p></footer>
</body>
</html>
```